affordable hand drawn art

Attempting to reach a consumer interested in affordable art to give as gifts, or to keep for themselves. Drawings to focus on beloved objects: homes, boats, cars...or loved personal photographs of...pets, friends and family. Attempting to reach customers with disposable income that may have not considered hand drawn art due to preconceived notions of cost/risk. The drawings would be guaranteed with payment due after seeing the finished product. No risk and all reward.

Target Market(s)

Adults with disposable income. New home/apartment buyers looking to decorate. People with treasured photographs. Sentimental personalities. Creative gift givers.

Industry/Entity Type

Consumer

Contact Information for Business Card

A photograph of a log cabin and on the flip-side a drawing of that photograph.

Font styles to use
Serif
Sans Serif

Requirements
Must have
• Contact information.
• Photograph w/drawing

```html
<!DOCTYPE html>
<html lang="en">
<head>
<meta charset="utf-8">
<title>Affordable Hand Drawn Art – Business Card</title>
<link href="https://fonts.googleapis.com/css2?family=Libre+Baskerville:wght@400;700&family=Caveat+Brush&family=Lato:wght@400;700&family=Marcellus&display=swap" rel="stylesheet">
<style>
  :root {
    --page: #ffffff;
    --card: #000000;
    --white: #ffffff;
    --panel-grey: #e6e6e6;
    --accent: #fb2a00;
    --ink: #333333;
    --photo-sky: #dfe9d3;
    --photo-roof: #56606a;
    --photo-wood: #9a7a55;
    --photo-grass: #4f9a2e;
    --drawing-sky: #e9dff0;
    --drawing-roof: #7d6fb8;
    --drawing-wood: #c89a6f;
    --drawing-leaf: #6aa85b;
  }
  * { box-sizing: border-box; margin: 0; padding: 0; }
  html, body { width: 1200px; height: 702px; overflow: hidden; background: var(--page); }
  .canvas { position: relative; width: 1200px; height: 702px; }

  /* Front card */
  .card-front {
    position: absolute; left: 20px; top: 17px; width: 614px; height: 380px;
    background: var(--card); border-radius: 28px;
  }
  .label {
    position: absolute; top: 6px; transform: translateX(-50%);
    font-family: "Libre Baskerville", serif; font-weight: 700; font-size: 14px;
    color: var(--white);
  }
  .label-photo { left: 181px; }
  .label-drawing { left: 450px; }
  .showcase {
    position: absolute; left: 31px; top: 31px; width: 553px; height: 317px;
    border: 2px solid var(--white); overflow: hidden; display: flex;
  }
  .photo-area {
    width: 290px; height: 100%;
    background: linear-gradient(180deg, var(--photo-sky) 0%, var(--photo-roof) 28%, var(--photo-wood) 55%, var(--photo-grass) 85%);
  }
  .drawing-area {
    flex: 1; height: 100%;
    background: linear-gradient(180deg, var(--drawing-sky) 0%, var(--drawing-roof) 30%, var(--drawing-wood) 58%, var(--drawing-leaf) 88%);
  }
  .tagline {
    position: absolute; left: 0; right: 0; bottom: 8px; text-align: center;
    color: var(--white); text-shadow: 0 0 4px #000, 0 0 2px #000;
  }
  .tagline-main { font-family: "Libre Baskerville", serif; font-weight: 700; font-size: 23px; line-height: 1.1; }
  .tagline-script { font-family: "Caveat Brush", cursive; font-weight: 400; font-size: 28px; }
  .tagline-sub { font-family: "Libre Baskerville", serif; font-size: 12px; }

  /* Back card */
  .card-back {
    position: absolute; left: 535px; top: 302px; width: 648px; height: 385px;
    background: var(--card); border-radius: 28px;
  }
  .back-sheet {
    position: absolute; left: 42px; top: 43px; width: 562px; height: 301px;
    background: var(--white);
  }
  .contact-list { position: absolute; left: 6px; top: 5px; width: 305px; }
  .contact-row {
    display: flex; align-items: center; height: 93px; margin-bottom: 5px;
    background: var(--panel-grey); padding-left: 18px;
  }
  .contact-icon {
    width: 57px; height: 57px; background: var(--accent);
    display: flex; align-items: center; justify-content: center; flex: none;
  }
  .contact-text {
    margin-left: 17px; font-family: "Lato", sans-serif; font-size: 12.5px;
    line-height: 1.35; color: var(--ink);
  }
  .name-panel {
    position: absolute; left: 316px; top: 5px; width: 242px; height: 290px;
    background: var(--accent); padding: 5px;
  }
  .name-frame {
    width: 100%; height: 100%; border: 1.5px solid var(--white);
    display: flex; flex-direction: column; align-items: center; justify-content: center;
    color: var(--white); text-align: center;
  }
  .name { font-family: "Marcellus", serif; font-size: 22px; letter-spacing: 0.5px; }
  .role { font-family: "Lato", sans-serif; font-size: 12.5px; margin-top: 4px; }
</style>
</head>
<body>
<div class="canvas">

  <section class="card-front">
    <span class="label label-photo">Photograph</span>
    <span class="label label-drawing">Drawing</span>
    <div class="showcase">
      <div class="photo-area" role="img" aria-label="Photograph of a log cabin among trees with green lawn and shrubs"></div>
      <div class="drawing-area" role="img" aria-label="Hand drawn coloured rendering of the same log cabin"></div>
      <div class="tagline">
        <div class="tagline-main">Affordable <span class="tagline-script">Hand drawn art</span></div>
        <div class="tagline-sub">(homes, boats, pets, friends....and more)</div>
      </div>
    </div>
  </section>

  <section class="card-back">
    <div class="back-sheet">
      <div class="contact-list">
        <div class="contact-row">
          <div class="contact-icon">
            <svg width="26" height="24" viewBox="0 0 26 24" aria-hidden="true">
              <path d="M13 1 L1 12 H4.5 V23 H10.5 V16 H15.5 V23 H21.5 V12 H25 Z" fill="#fff"/>
            </svg>
          </div>
          <p class="contact-text">214 N.Birchwood Lane,<br>Cedar Bay,Mi 49800</p>
        </div>
        <div class="contact-row">
          <div class="contact-icon">
            <svg width="24" height="24" viewBox="0 0 24 24" aria-hidden="true">
              <path d="M6.6 10.8c1.4 2.8 3.8 5.1 6.6 6.6l2.2-2.2c.3-.3.7-.4 1-.2 1.1.4 2.3.6 3.6.6.6 0 1 .4 1 1V20c0 .6-.4 1-1 1C10.6 21 3 13.4 3 4c0-.6.4-1 1-1h3.5c.6 0 1 .4 1 1 0 1.3.2 2.5.6 3.6.1.3 0 .7-.2 1z" fill="#fff"/>
            </svg>
          </div>
          <p class="contact-text">555.014.2287</p>
        </div>
        <div class="contact-row">
          <div class="contact-icon">
            <svg width="28" height="20" viewBox="0 0 28 20" aria-hidden="true">
              <rect x="1" y="1" width="26" height="18" fill="none" stroke="#fff" stroke-width="2"/>
              <path d="M1 1 L14 11 L27 1 M1 19 L10.5 9 M27 19 L17.5 9" fill="none" stroke="#fff" stroke-width="2"/>
            </svg>
          </div>
          <p class="contact-text">owenharlow@mailbox.com</p>
        </div>
      </div>
      <div class="name-panel">
        <div class="name-frame">
          <p class="name">OWEN HARLOW</p>
          <p class="role">Artist</p>
        </div>
      </div>
    </div>
  </section>

</div>
</body>
</html>
```